Web Design Project

*** This project has been temporarily placed on hold as the Logo Design needs to be completed first. You are all welcome to participate on it as well: http://gigs.pitchboardly.com/brief.aspx?id=482917 This project will be reopened soon***

Revamp current website adding newly designed logo and creating layout that is good on desktops, tablets, and cell phones.

Current website can be viewed at www.vennatistudio.com

Will you see the website is small but graphics heavy in the gallery. The gallery needs to be setup so that it is easy to maintain the links and update the photos.

Needs to have high visual impact.

I need a new logo and website layout designed for my partner's business. This is a birthday present. His business is interior painting, wallpapering and design. He also has access to a wide variety of products including carpet, fabrics, furniture, wallpaper, tile, countertops, etc. I have attached some screen shots of his website for reference. He is a one man shop and has a stellar reputation with his customers. He is on-time, very tidy, excellent with animals, and always finishes on time and on budget. There are no restrictions on colors or fonts. The logo needs to work well with the website, business cards and printed materials. The website needs to flow content for device size so it looks just as good on a cell phone or tablet as it does on a desktop computer. Whatever the heck that's called! Thanks. I am looking forward to seeing everyone's ideas.
Updates

Hi Designers, We've reopened this project as our logo design project has just completed. Please refer to the uploaded files and make use of either Horizontal or Vertical versions of the logo depending on what you think is suitable for your design proposals. We look forward to your creative submissions!

Target Market(s)

Consumers looking for interior design, painting, and wallpapering as well as interior products such as flooring, window treatments, reupholstering, counter tops, etc.

Industry/Entity Type

Cell Phone

Requirements
Must have
• Clean, sharp, visual impact (at least on the home page)
Should not have
• Clutter.

```html
<!DOCTYPE html>
<html lang="en">
<head>
<meta charset="utf-8">
<title>Vennati Interior Designs</title>
<link href="https://fonts.googleapis.com/css2?family=Questrial&family=Arimo:wght@400&family=Pinyon+Script&display=swap" rel="stylesheet">
<style>
  :root {
    --brand-red: #8a1420;
    --brand-red-dark: #6e0e18;
    --text: #111111;
    --nav-text: #1a1a1a;
    --rule: #cfcfcf;
    --footer-bg: #363636;
    --footer-text: #ffffff;
    --page-bg: #f2f2f2;
  }
  * { box-sizing: border-box; margin: 0; padding: 0; }
  html, body { width: 1200px; height: 1051px; overflow: hidden; }
  body {
    position: relative;
    background: radial-gradient(ellipse at 50% 45%, #ffffff 0%, #f4f4f4 55%, #e9e9e9 100%);
    font-family: "Arimo", Arial, sans-serif;
    color: var(--text);
  }
  .brand {
    position: absolute; top: 40px; left: 0; width: 1200px;
    text-align: center;
    font-family: "Questrial", sans-serif;
    font-size: 40px; letter-spacing: 1px;
    color: var(--brand-red);
  }
  .main-nav {
    position: absolute; top: 140px; left: 127px; width: 943px; height: 37px;
    border-bottom: 1px solid var(--rule);
    font-family: "Questrial", sans-serif; font-size: 16px;
  }
  .main-nav a {
    position: absolute; top: 0; height: 36px; line-height: 36px;
    color: var(--nav-text); text-decoration: none; text-align: center;
    transform: translateX(-50%); white-space: nowrap;
  }
  .main-nav a.is-active {
    width: 79px; background: linear-gradient(#a01a27, var(--brand-red-dark));
    color: #fff; border-radius: 4px 4px 0 0;
  }
  .gallery-item {
    position: absolute; border: 1px solid #8c8c8c; border-radius: 3px;
    box-shadow: 0 1px 3px rgba(0,0,0,.25);
  }
  .gallery-item svg { position: absolute; left: 50%; top: 50%; transform: translate(-50%,-50%); }
  .divider {
    position: absolute; top: 730px; left: 200px; width: 800px; height: 1px;
    background: linear-gradient(90deg, transparent, #d0d0d0, transparent);
  }
  .welcome-title {
    position: absolute; top: 762px; left: 0; width: 1200px; text-align: center;
    font-family: "Pinyon Script", cursive; font-size: 46px; font-weight: 400;
    color: var(--brand-red);
  }
  .welcome-copy {
    position: absolute; top: 815px; left: 125px; width: 936px;
    text-align: center; font-size: 13.4px; line-height: 22px;
  }
  .welcome-copy p + p { margin-top: 22px; }
  .site-footer {
    position: absolute; top: 1002px; left: 0; width: 1200px; height: 49px;
    background: var(--footer-bg); color: var(--footer-text); font-size: 12.5px;
  }
  .site-footer span { position: absolute; top: 16px; }
  .footer-copy { left: 105px; }
  .footer-address { right: 137px; }
</style>
</head>
<body>
  <div class="brand">Vennati Interior Designs</div>

  <nav class="main-nav">
    <a class="is-active" style="left:143px">HOME</a>
    <a style="left:270px">ABOUT US</a>
    <a style="left:408px">CONTACT</a>
    <a style="left:540px">GALLERY</a>
    <a style="left:675px">PRODUCTS</a>
    <a style="left:813px">SERVICES</a>
  </nav>

  <div class="gallery-item" role="img" aria-label="Kitchen with red cabinets and steel cooktop" style="left:95px;top:205px;width:174px;height:215px;background:linear-gradient(160deg,#e8eef2,#a62030 60%,#5a0e14)"></div>
  <div class="gallery-item" role="img" aria-label="Room with French doors and wood floor" style="left:303px;top:205px;width:163px;height:231px;background:linear-gradient(180deg,#ece6d8,#d8c7a6 55%,#8a5a32)"></div>
  <div class="gallery-item" role="img" aria-label="Red living room with sofa, zoom on hover" style="left:500px;top:206px;width:174px;height:139px;background:linear-gradient(180deg,#b02a3c,#8e1a2a)">
    <svg width="52" height="52" viewBox="0 0 52 52" aria-hidden="true">
      <circle cx="22" cy="22" r="17" fill="none" stroke="#fff" stroke-width="5"/>
      <line x1="34" y1="34" x2="46" y2="46" stroke="#fff" stroke-width="8" stroke-linecap="round"/>
      <line x1="13" y1="22" x2="31" y2="22" stroke="#fff" stroke-width="4"/>
      <line x1="22" y1="13" x2="22" y2="31" stroke="#fff" stroke-width="4"/>
    </svg>
  </div>
  <div class="gallery-item" role="img" aria-label="Dining room with orange wooden table" style="left:709px;top:206px;width:174px;height:252px;background:linear-gradient(170deg,#c9a57a,#b24a22 60%,#d9c4b0)"></div>
  <div class="gallery-item" role="img" aria-label="Lounge with colourful striped sofa" style="left:920px;top:206px;width:174px;height:230px;background:linear-gradient(160deg,#f0eeee,#c63a55 45%,#c7c94a 80%,#e6e0d6)"></div>
  <div class="gallery-item" role="img" aria-label="White living room with orange cushion" style="left:94px;top:455px;width:174px;height:173px;background:linear-gradient(180deg,#d8d8d8,#f2f2f2 60%,#7a7a7a)"></div>
  <div class="gallery-item" role="img" aria-label="Dining room with marble wall and black chairs" style="left:302px;top:496px;width:165px;height:132px;background:linear-gradient(180deg,#e6e3df,#cfcac3 55%,#3a3a3a)"></div>
  <div class="gallery-item" role="img" aria-label="White bathroom with round mirror" style="left:499px;top:391px;width:174px;height:172px;background:linear-gradient(180deg,#f1f0ee,#dcdad6 65%,#2c2c2c)"></div>
  <div class="gallery-item" role="img" aria-label="Bright living room with blue sofa" style="left:707px;top:501px;width:176px;height:176px;background:linear-gradient(180deg,#eeeae2,#d2ccc0 55%,#8fb2b8)"></div>
  <div class="gallery-item" role="img" aria-label="Airy room with yellow and green sofas" style="left:918px;top:477px;width:177px;height:217px;background:linear-gradient(180deg,#f4f4f4,#e2e2dc 55%,#c8c13a 80%,#dcdcd6)"></div>

  <div class="divider"></div>

  <h1 class="welcome-title">Welcome to Vennati Interior Designs.</h1>
  <div class="welcome-copy">
    <p>With the various materials, colors, and finishes available the choices today can be daunting. By listening to you, I am able to pick just the right color, the right fabric, or the right furniture for your projects. Whether you are starting with a small project or a large project, I am ready to bring your ideas to life. It doesn't take a big budget to achieve dramatic effects. A wonderful new look is within anyone's reach.</p>
    <p>My guidance with the selection of colors, fabrics, paint, wallpaper, and furniture, as well as the placement of items in a room, will help you achieve the results you desire – a beautiful home that is a joy to walk into and to show off!</p>
  </div>

  <footer class="site-footer">
    <span class="footer-copy">Copyright © Vennati Interior Designs. All rights reserved.</span>
    <span class="footer-address">2410 W Linden Ct. • Merriam, KS 66203 • (913) 555-0182</span>
  </footer>
</body>
</html>
```